NEW Brand "New Zealand Wine Estate"

We are looking for a design for our new range of New Zealand wine. An estate label that can be used for several varietals.
We have three potential names...
Hollow Pine Estate
Velvet Morrow Estate
Tovrina Estate
first variant is "Central Otago Pinot Noir" please use this in the original design.
This brand is for world export, so will need to be appealing to many markets but representative of New Zealand and our rugged Coasts.
Target Market(s)
Supermarket $25 NZD per bottle price point. Young and hip
Font styles to use
Decorative
Script
Requirements
Must have
- Sophistication but edgy. Stand out on a shelf.
- the brand needs to be able to be used for red or white wine.

```html
<!DOCTYPE html>
<html lang="en">
<head>
<meta charset="utf-8">
<title>Tovrina Estate – Wine Labels</title>
<link rel="stylesheet" href="https://fonts.googleapis.com/css2?family=Abril+Fatface&family=Montserrat:wght@500&family=Playfair+Display+SC:wght@700&display=swap">
<style>
  :root {
    --stage-light: #ecebe6;
    --stage-warm: #ddd6cb;
    --white-label-top: #9a87a6;
    --white-label-mid: #7a5f84;
    --white-label-base: #4a2c4f;
    --white-badge: #6e4d72;
    --red-label-top: #b9cdbf;
    --red-label-mid: #5f8a86;
    --red-label-base: #243f42;
    --red-badge: #3f5f61;
    --ink-light: #f7f3ec;
  }
  * { margin: 0; padding: 0; box-sizing: border-box; }
  html, body { width: 1200px; height: 753px; overflow: hidden; }
  .canvas { display: flex; width: 1200px; height: 753px; }
  .stage {
    position: relative;
    width: 600px; height: 753px;
    display: flex; justify-content: center; align-items: center;
  }
  .stage--white { background: var(--stage-light); }
  .stage--red { background: var(--stage-warm); }

  .label {
    position: relative;
    width: 300px; height: 450px;
    margin-top: 60px;
    color: var(--ink-light);
    text-align: center;
  }
  .label__scene { position: absolute; inset: 0; }
  .label--white .label__scene {
    background:
      radial-gradient(circle at 84% 18%, #f3e9b8 0 48px, rgba(243,233,184,0) 50px),
      linear-gradient(180deg, var(--white-label-top) 0%, #b8aec6 45%, var(--white-label-mid) 72%, var(--white-label-base) 100%);
  }
  .label--red .label__scene {
    background:
      radial-gradient(circle at 84% 18%, #f4edbd 0 48px, rgba(244,237,189,0) 50px),
      linear-gradient(180deg, var(--red-label-mid) 0%, var(--red-label-top) 45%, var(--red-label-mid) 72%, var(--red-label-base) 100%);
  }

  .label__badge {
    position: absolute;
    top: -46px; left: 50%;
    transform: translateX(-50%);
    width: 120px; height: 110px;
    border: 3px solid var(--ink-light);
    display: flex; align-items: center; justify-content: center;
    font-family: "Abril Fatface", serif;
    font-size: 25px;
    color: var(--ink-light);
  }
  .label--white .label__badge { background: var(--white-badge); }
  .label--red .label__badge { background: var(--red-badge); }

  .label__name {
    position: absolute;
    top: 160px; left: 0; right: 0;
    font-family: "Abril Fatface", serif;
    font-size: 42px;
    line-height: 40px;
  }
  .label__region {
    position: absolute;
    top: 305px; left: 0; right: 0;
    font-family: "Montserrat", sans-serif;
    font-size: 8px;
    letter-spacing: 0.08em;
    text-transform: uppercase;
  }
  .label__varietal {
    position: absolute;
    top: 318px; left: 0; right: 0;
    font-family: "Playfair Display SC", serif;
    font-size: 17px;
    letter-spacing: 0.06em;
  }
  .label__footer {
    position: absolute;
    bottom: 12px; left: 12px; right: 12px;
    display: flex; justify-content: space-between; align-items: baseline;
    font-family: "Montserrat", sans-serif;
    font-size: 11px;
  }
  .label__vintage {
    font-family: "Abril Fatface", serif;
    font-size: 18px;
    letter-spacing: 0.04em;
  }
</style>
</head>
<body>
<main class="canvas">
  <section class="stage stage--white">
    <article class="label label--white">
      <div class="label__scene" role="img" aria-label="Dusk illustration in violet tones: full moon, soaring bird, distant mountains and pine silhouettes over grass"></div>
      <div class="label__badge">Tovrina</div>
      <h1 class="label__name">Tovrina<br>Estate</h1>
      <p class="label__region">Central Otago</p>
      <p class="label__varietal">MANZANILLA</p>
      <div class="label__footer">
        <span>75cl</span>
        <span class="label__vintage">2016</span>
        <span>15% vol.</span>
      </div>
    </article>
  </section>
  <section class="stage stage--red">
    <article class="label label--red">
      <div class="label__scene" role="img" aria-label="Dusk illustration in teal tones: full moon, soaring bird, distant mountains and pine silhouettes over grass"></div>
      <div class="label__badge">Tovrina</div>
      <h1 class="label__name">Tovrina<br>Estate</h1>
      <p class="label__region">Central Otago</p>
      <p class="label__varietal">PINOT NOIR</p>
      <div class="label__footer">
        <span>75cl</span>
        <span class="label__vintage">2016</span>
        <span>15% vol.</span>
      </div>
    </article>
  </section>
</main>
</body>
</html>
```